Handouts in brochure which included about our services, magnet card and emergency sticker design

We need a brochure packaging design for our company which is based in Australia. We are a home appliance services company based in Melbourne. We provide mainly three core services, Electrician, plumbing and building services/handyman.

We wish to include the following things in the brochure package we send to our customers :
1. About our services (4 sided bi fold design)
2. Magnet card
3. Emergency sticker for one of our services

We have already made a rough design of the content for each for this, however it needs designing and editing.

I have attached the files for your reference. You can visit http://quorvell.net.au/
for more information.

Target Market(s)

30 to 40 years

Industry/Entity Type

Appliance

Font styles to use
Serif
Sans Serif

Colors
3176b5
fbed22
0456a4

Requirements
Must have
• Home
Nice to have
• Cars

```html
<!DOCTYPE html>
<html lang="en">
<head>
<meta charset="utf-8">
<title>Quorvell Electricians – Brochure Spread</title>
<link href="https://fonts.googleapis.com/css2?family=Josefin+Sans:wght@300;400;600;700&display=swap" rel="stylesheet">
<style>
  :root{
    --blue-deep:#0456a4;
    --blue-mid:#3176b5;
    --blue-royal:#1a56a8;
    --cyan:#3fc3ef;
    --yellow:#fbd90f;
    --ink:#333a40;
    --paper:#ffffff;
    --backdrop:#e9eaeb;
  }
  *{margin:0;padding:0;box-sizing:border-box}
  html,body{width:1200px;height:859px;overflow:hidden;background:var(--backdrop)}
  body{font-family:"Josefin Sans",sans-serif;color:var(--ink)}
  .canvas{position:relative;width:1200px;height:859px}
  .spread-shapes{position:absolute;left:0;top:0;width:1200px;height:859px}
  .abs{position:absolute}

  .cover-intro{left:128px;top:104px;width:230px;color:var(--paper);font-weight:300;font-size:24px;line-height:28px}

  .about{left:134px;top:326px;width:416px}
  .about h2{font-weight:400;font-size:16px;margin-bottom:6px;color:#3a3f44}
  .about p{font-weight:300;font-size:8.6px;line-height:12.5px;text-align:justify;margin-bottom:12px}
  .about ul{list-style:none;margin:-2px 0 11px;font-weight:600;font-size:8.6px;line-height:12.5px}
  .about li::before{content:"\25CF";font-size:6px;margin-right:3px;vertical-align:1px}

  .contact{right:622px;top:727px;text-align:right;font-size:10px;line-height:13.8px;color:#222;font-weight:400;font-style:normal}
  .contact .label{text-transform:uppercase}

  .brand{left:626px;top:92px;color:var(--paper);font-weight:700;font-size:46px;letter-spacing:-1px}

  .headline{left:660px;top:553px;width:424px;text-align:center;color:var(--blue-royal);line-height:1}
  .headline .city{display:block;font-weight:700;font-size:52px}
  .headline .trade{display:block;font-weight:300;font-size:33px;margin-top:2px}
  .headline .trade small{font-size:27px}
  .headline .focus{display:block;font-weight:700;font-size:35px;margin-left:60px}
  .headline .focus .amp{font-weight:300}
  .headline .services{display:block;font-weight:700;font-size:33px;margin-left:-20px}

  .web{right:110px;top:762px;color:var(--paper);font-weight:600;font-size:15px}
</style>
</head>
<body>
<div class="canvas">
  <svg class="spread-shapes" viewBox="0 0 1400 1002" preserveAspectRatio="none">
    <defs>
      <linearGradient id="houseTone" x1="0" y1="0" x2="0" y2="1">
        <stop offset="0" stop-color="#dfe6ea"/>
        <stop offset="0.55" stop-color="#c7cfc8"/>
        <stop offset="1" stop-color="#4f7a34"/>
      </linearGradient>
      <linearGradient id="portraitTone" x1="0" y1="0" x2="0" y2="1">
        <stop offset="0" stop-color="#e4e0dd"/>
        <stop offset="1" stop-color="#c9bcb2"/>
      </linearGradient>
      <linearGradient id="vanTone" x1="0" y1="0" x2="1" y2="0">
        <stop offset="0" stop-color="#2a5ea8"/>
        <stop offset="1" stop-color="#dfe6ee"/>
      </linearGradient>
      <filter id="pageShadow" x="-5%" y="-5%" width="110%" height="110%">
        <feDropShadow dx="3" dy="4" stdDeviation="4" flood-color="#000" flood-opacity="0.25"/>
      </filter>
    </defs>

    <rect x="98" y="75" width="1206" height="853" fill="#fff" filter="url(#pageShadow)"/>

    <polygon points="98,75 425,75 425,325 98,280" fill="var(--blue-deep)"/>
    <polygon points="425,75 700,75 700,300 425,325" fill="url(#portraitTone)" role="img" aria-label="Portrait photo of a smiling electrician in a blue work shirt"/>
    <polygon points="98,280 700,355 700,395" fill="var(--cyan)"/>
    <polygon points="98,280 425,325 560,312 700,355" fill="#fff"/>
    <polygon points="525,334 700,290 700,358" fill="var(--yellow)"/>
    <polygon points="425,325 525,334 700,290 700,300" fill="#fff"/>

    <polygon points="98,818 480,928 98,928" fill="var(--yellow)"/>
    <polygon points="98,838 440,928 98,928" fill="var(--blue-royal)"/>
    <polygon points="98,866 330,928 98,928" fill="var(--blue-mid)"/>

    <polygon points="700,75 1305,75 1305,95 700,262" fill="var(--blue-royal)"/>
    <polygon points="990,168 1305,75 1305,98 1060,160" fill="var(--cyan)"/>
    <polygon points="1100,160 1305,100 1305,202" fill="var(--yellow)"/>
    <polygon points="1195,180 1305,150 1305,212" fill="var(--blue-royal)"/>
    <polygon points="700,268 1180,158 1305,205 1305,522 700,590" fill="url(#houseTone)" role="img" aria-label="Photo of a large white two-storey home with rounded balconies, palm trees and a landscaped garden"/>

    <polygon points="700,572 850,622 700,655" fill="var(--yellow)"/>
    <polygon points="700,655 890,612 1200,520 1305,520 1305,528 700,697" fill="var(--blue-royal)"/>
    <polygon points="1060,572 1305,520 1305,662" fill="var(--blue-royal)"/>
    <polygon points="1090,578 1305,612 1305,640" fill="var(--yellow)"/>

    <polygon points="960,928 1305,812 1305,836 1020,928" fill="var(--yellow)"/>
    <polygon points="1000,928 1305,846 1305,928" fill="var(--blue-royal)"/>

    <rect x="712" y="808" width="284" height="114" fill="url(#vanTone)" role="img" aria-label="Photo of the branded company service van"/>
  </svg>

  <h1 class="abs cover-intro">Quorvell Electricians Melbourne – Great Electrical Services &amp; Customer Care.</h1>

  <section class="abs about">
    <h2>About Us:</h2>
    <p>It takes years to become a licensed electrician, even then, the learning and training never stops. The Quorvell team of electricians in Melbourne are expertly trained and experienced in all aspects of electrical services and safety. Each team member is fully employed by us. This is a really important factor to us and we believe it matters to YOU too. Working within a team who have the same goals and ambitions in mind helps us to deliver the best electrical services to YOU.</p>
    <p>Quorvell is a family owned and operated business based in Richmond. With more than 20 years of continuous service to our industry and to the suburbs of Richmond, East Melbourne, South Yarra, Camberwell, Windsor etc, we continue to foster and uphold our founding principles:</p>
    <ul>
      <li>Safety first</li>
      <li>Ongoing training for every member of our staff</li>
      <li>Keeping you informed through ongoing communications</li>
      <li>Knowing you as a name, not a number</li>
      <li>Respecting you and your home as if you were family...because in a way, you are</li>
      <li>Service with a smile</li>
    </ul>
    <p>We deliver electrical services and repairs to local family home, offices, restaurants and factories everyday around Melbourne, ensuring the safety of your family, loved ones, staff and colleagues are handled with the utmost attention. Our electrical services include full or part house wiring, smoke detectors, home security systems, data wiring, security lighting indoors and out and much more.. We're confident that if you try us once you'll want us back the next time you need an electrician.</p>
    <p>For the team at Quorvell Electricians no job is too BIG or too Small. We believe we have the best team of electricians Melbourne has to offer and we're up for the toughest electrical repairs and installation jobs. Our primary electrical jobs come from our Residential Customers, home owners who need assistance quickly and at an affordable price. We're there when you need us and if you need Emergency Electrical Services too. We also cater to Commercial Electrical Services and Repairs and are happy to service many of the local businesses within our area.</p>
  </section>

  <address class="abs contact">
    <span class="label">Contact Info</span><br>
    Quorvell Electricians 27 Halden St<br>
    Richmond, VIC 3121<br>
    Phone: (03) 9000 4812
  </address>

  <div class="abs brand">Quorvell</div>

  <h2 class="abs headline">
    <span class="city">Melbourne</span>
    <span class="trade">Electrical Contractor <small>for</small></span>
    <span class="focus">Repairs <span class="amp">&amp;</span> Security</span>
    <span class="services">Services</span>
  </h2>

  <div class="abs web">www.quorvell.net.au</div>
</div>
</body>
</html>
```